Business card design for Bront Engineering Qavo

We need a new business card design along with all the necessary to place an order. The company is Bront Engineering Qavo and we recently updated our logo.

```html
<!DOCTYPE html>
<html lang="en">
<head>
<meta charset="utf-8">
<title>Bront Engineering Qavo – Business Card</title>
<link rel="stylesheet" href="https://fonts.googleapis.com/css2?family=Exo+2:wght@300;400;600;700&display=swap">
<style>
  :root {
    --backdrop: #ababab;
    --card-dark: #121212;
    --card-light: #ffffff;
    --brand-yellow: #e2b827;
    --brand-grey: #8f8f8f;
    --text-grey: #8a8a8a;
    --ink: #0c0c0c;
  }
  * { margin: 0; padding: 0; box-sizing: border-box; }
  html, body {
    width: 1200px; height: 1000px; overflow: hidden;
    background: var(--backdrop);
    font-family: "Exo 2", sans-serif;
  }
  .card {
    position: absolute;
    width: 694px; height: 400px;
    border-radius: 28px;
    overflow: hidden;
  }
  .card--front { left: 249px; top: 87px; background: var(--card-dark); }
  .card--back { left: 248px; top: 518px; background: var(--card-light); text-align: center; }

  .wordmark {
    display: flex; align-items: center; gap: 10px;
    font-weight: 600; color: var(--brand-grey);
    white-space: nowrap;
  }
  .wordmark__dot {
    width: 14px; height: 14px; border-radius: 50%;
    background: var(--brand-yellow); flex: none;
  }
  .card--front .wordmark { position: absolute; left: 70px; top: 190px; font-size: 30px; }
  .website {
    position: absolute; left: 109px; top: 265px;
    font-size: 16px; letter-spacing: 1px; color: var(--brand-grey);
  }
  .website__domain { color: var(--brand-yellow); font-weight: 700; }

  .card--back .wordmark {
    position: absolute; left: 0; right: 0; top: 90px;
    justify-content: center; font-size: 30px;
  }
  .person__name {
    position: absolute; left: 0; right: 0; top: 172px;
    font-size: 26px; font-weight: 700; color: var(--ink);
  }
  .person__role {
    position: absolute; left: 0; right: 0; top: 206px;
    font-size: 14px; letter-spacing: 3.5px; color: var(--text-grey);
  }
  .contact-icons {
    position: absolute; left: 0; right: 0; top: 240px;
    display: flex; justify-content: center; gap: 4px;
  }
  .contact-icons svg { width: 26px; height: 26px; }
  .contact {
    position: absolute; left: 0; right: 0;
    font-size: 20px; font-weight: 300; color: var(--text-grey);
  }
  .contact--phone { top: 272px; }
  .contact--email { top: 296px; }
  .divider {
    position: absolute; left: 287px; top: 334px;
    width: 120px; height: 3px; background: var(--brand-yellow);
  }
  .contact--address { top: 344px; }
</style>
</head>
<body>
  <section class="card card--front">
    <div class="wordmark"><span class="wordmark__dot"></span>Bront Engineering Qavo</div>
    <p class="website"><span class="website__domain">brontengineering</span>.co.uk</p>
  </section>

  <section class="card card--back">
    <div class="wordmark"><span class="wordmark__dot"></span>Bront Engineering Qavo</div>
    <h1 class="person__name">Name Surname</h1>
    <p class="person__role">POSITION</p>
    <div class="contact-icons">
      <svg viewBox="0 0 26 26" aria-label="Phone">
        <circle cx="13" cy="13" r="13" fill="#e2b827"/>
        <path d="M9.2 6.8l2 2.2c.4.4.4 1 0 1.4l-1 1c.8 1.7 2 2.9 3.7 3.7l1-1c.4-.4 1-.4 1.4 0l2.2 2c.4.4.4 1 0 1.4l-1.1 1.1c-.6.6-1.5.7-2.2.3-3-1.6-5.3-3.9-6.9-6.9-.4-.7-.3-1.6.3-2.2l1.2-1c.4-.4 1-.4 1.4 0z" fill="#fff"/>
      </svg>
      <svg viewBox="0 0 26 26" aria-label="Email">
        <circle cx="13" cy="13" r="13" fill="#e2b827"/>
        <rect x="6.5" y="8.5" width="13" height="9" rx="1" fill="#fff"/>
        <path d="M7 9l6 5 6-5" fill="none" stroke="#e2b827" stroke-width="1.2"/>
      </svg>
    </div>
    <p class="contact contact--phone">01632 960418</p>
    <p class="contact contact--email">sales@brontengineering.co.uk</p>
    <div class="divider"></div>
    <p class="contact contact--address">24 Harlow Court, Kettering NN15 6XT</p>
  </section>
</body>
</html>
```